Business Card Design for Brightkeel

The company provides engineering tender consulting services and personnel resources. The target market is large engineering construction and services companies. The business is based in Australia.

```html
<!DOCTYPE html>
<html lang="en">
<head>
<meta charset="utf-8">
<title>Brightkeel Business Card</title>
<link href="https://fonts.googleapis.com/css2?family=Quicksand:wght@500&family=Marcellus+SC&display=swap" rel="stylesheet">
<style>
  :root {
    --sky: #a3d8f5;
    --band: #2b2a29;
    --ink: #2e2e2e;
    --white: #ffffff;
    --bg-centre: #ffffff;
    --bg-edge: #d9d9d9;
  }
  html, body {
    margin: 0;
    padding: 0;
    overflow: hidden;
  }
  .stage {
    position: relative;
    width: 1165px;
    height: 1200px;
    overflow: hidden;
    background: radial-gradient(ellipse at 50% 50%, var(--bg-centre) 45%, var(--bg-edge) 100%);
    font-family: "Quicksand", sans-serif;
  }
  .card {
    position: absolute;
    left: 179px;
    width: 807px;
    height: 490px;
    background: var(--sky);
  }
  .card--front { top: 58px; }
  .card--back { top: 604px; }
  .band {
    position: absolute;
    left: 0;
    width: 469px;
    height: 121px;
    background: var(--band);
    box-shadow: 6px 8px 10px rgba(0, 0, 0, 0.28);
    color: var(--white);
  }
  .card--front .band { top: 170px; }
  .card--back .band { top: 169px; }
  .brand {
    position: absolute;
    left: 44px;
    top: 24px;
    font-weight: 500;
    font-size: 46px;
    line-height: 1;
    letter-spacing: 1px;
  }
  .tagline {
    position: absolute;
    left: 44px;
    top: 82px;
    font-weight: 500;
    font-size: 14.5px;
    letter-spacing: 1.2px;
    text-transform: uppercase;
  }
  .person-name {
    position: absolute;
    left: 46px;
    top: 22px;
    font-family: "Marcellus SC", serif;
    font-size: 40px;
    letter-spacing: 2px;
    line-height: 1;
  }
  .person-role {
    position: absolute;
    left: 0;
    width: 469px;
    top: 72px;
    text-align: center;
    padding-left: 20px;
    box-sizing: border-box;
    font-family: "Marcellus SC", serif;
    font-size: 21px;
    letter-spacing: 1.5px;
  }
  .contact, .address {
    position: absolute;
    margin: 0;
    color: var(--ink);
    font-weight: 500;
    font-size: 22px;
    line-height: 31px;
    letter-spacing: 1.5px;
  }
  .contact { left: 46px; top: 348px; }
  .address { right: 45px; top: 360px; text-align: right; font-size: 20px; line-height: 28px; }
  .contact-email { text-transform: uppercase; font-size: 19px; }
</style>
</head>
<body>
<main class="stage">
  <section class="card card--front" aria-label="Card front">
    <div class="band">
      <div class="brand">Brightkeel</div>
      <div class="tagline">Engineering Consulting Services</div>
    </div>
  </section>

  <section class="card card--back" aria-label="Card back">
    <div class="band">
      <div class="person-name">Marcus Harlow</div>
      <div class="person-role">President</div>
    </div>
    <p class="contact">
      M: +614 555 018<br>
      T: +612 555 730<br>
      E: <span class="contact-email">mharlow@nnn.com.au</span>
    </p>
    <p class="address">
      PO Box 99 Nnnnnnnnnn<br>
      Nnn, 9999<br>
      ABN99999999999
    </p>
  </section>
</main>
</body>
</html>
```